Need Landing Page for Data Security Company

Need a new landing page (PSD) for our data security company (www.korvadel.com). We specialize in selling patented hard drive destruction machines that guarantee the data on your hard drives are unrecoverable. We have several large clients such as Lumigrove, Chirpaloo and Vendrix just to name a few. Really want to have a landing page that sticks out.

Attached is a one pager we use just for emailing clients. We do not want the landing page to look like this. This is just for content to read. The landing page needs

Target Market(s)

Government, business corporations, IT decision makers. Not every day user

Industry/Entity Type

It Company

Number of Pages Required

1 page

Font styles to use
Other font styles liked:
• Match Current Website

Requirements
Must have
• Its a landing page so it needs a Contact us Section at the very top!!!
• Need to be a very attractive landing page.. Would like a mix of showcasing our products and also having some client list to show our bigger name clients (lumigrove, vendrix, chirpaloo)
• Landing page needs to use the same color/style schema as current website. Also will be using the same menu structure as what exists today.
• www.korvadel.com
Nice to have
• Maybe some streamvault videos of our products?

```html
<!DOCTYPE html>
<html lang="en">
<head>
<meta charset="utf-8">
<title>Korvadel Technologies</title>
<link href="https://fonts.googleapis.com/css2?family=Open+Sans:wght@400;600;700&family=Raleway:wght@500;600;700&display=swap" rel="stylesheet">
<style>
:root{
  --green:#8cc63e;
  --green-dark:#6da52a;
  --black:#0e0e0e;
  --dark:#1a1a1a;
  --panel:#222;
  --text:#555;
  --light:#f4f4f4;
  --white:#fff;
}
*{box-sizing:border-box;margin:0;padding:0}
html,body{width:1200px;height:2376px;overflow:hidden}
body{font-family:"Open Sans",Arial,sans-serif;color:var(--text);background:var(--white);position:relative}
.brand-name{font-family:"Raleway",Arial,sans-serif;font-weight:700;color:var(--green)}
/* header */
.site-header{position:absolute;top:0;left:0;width:1200px;height:152px;background:var(--black)}
.logo{position:absolute;left:60px;top:20px;display:flex;align-items:center;gap:10px}
.logo-mark{width:22px;height:22px;background:var(--green)}
.logo .brand-name{font-size:36px;line-height:1}
.logo-tag{position:absolute;left:92px;top:62px;font-size:10px;color:#aaa;letter-spacing:1px}
.header-call{position:absolute;right:70px;top:22px;display:flex;align-items:center;gap:12px;color:var(--white)}
.header-call small{display:block;font-size:11px;color:#bbb}
.header-call strong{font-size:26px;font-weight:600;color:var(--white)}
.phone-icon{width:40px;height:40px;border-radius:50%;border:2px solid var(--green);display:flex;align-items:center;justify-content:center}
.main-nav{position:absolute;top:110px;left:150px;width:900px;display:flex;justify-content:space-between}
.main-nav a{font-size:13px;color:#ddd;text-decoration:none;padding:8px 20px}
.main-nav a.active{background:var(--green);color:var(--white)}
/* hero */
.hero{position:absolute;top:152px;left:0;width:1200px;height:408px;background:radial-gradient(circle at 30% 40%,#d9f1a8 0,#a9d85a 35%,#6ea82b 75%,#4d7d1b 100%)}
.hero-content{position:absolute;top:90px;width:100%;text-align:center}
.hero-brand{display:inline-flex;align-items:center;gap:12px;background:rgba(255,255,255,.85);padding:18px 30px}
.hero-brand .brand-name{font-size:40px;color:#222}
.hero-brand .logo-mark{width:28px;height:28px}
.hero h1{font-family:"Raleway",Arial,sans-serif;font-size:30px;font-weight:600;color:#1d1d1d;margin-top:40px}
.hero p{font-size:14px;color:#2a2a2a;margin-top:6px}
.hero-arrow{position:absolute;top:180px}
/* features */
.features{position:absolute;top:560px;left:0;width:1200px;height:300px;background:var(--white);display:flex;justify-content:center;gap:60px;padding-top:50px}
.feature{width:280px;text-align:center}
.feature h3{font-size:14px;font-weight:600;color:var(--green);margin:14px 0 8px;line-height:1.3}
.feature p{font-size:11px;line-height:1.6}
.btn{display:inline-block;background:var(--green);color:var(--white);font-size:11px;font-weight:700;padding:8px 16px;margin-top:14px}
.btn-outline{display:inline-block;border:1px solid var(--green);color:var(--white);font-size:11px;font-weight:600;padding:8px 16px;margin-top:16px}
/* section title */
.section-title{display:flex;align-items:center;justify-content:center;gap:16px;font-family:"Raleway",Arial,sans-serif;font-size:24px;font-weight:700;color:var(--green)}
.section-title::before,.section-title::after{content:"";width:60px;height:1px;background:var(--green)}
/* about */
.about{position:absolute;top:860px;left:0;width:1200px;height:300px;background:linear-gradient(100deg,#2f2f2f 0,#151515 40%,#0c0c0c 100%)}
.about-content{position:absolute;top:70px;left:300px;width:600px;text-align:center}
.about p{color:#ccc;font-size:12px;line-height:1.7;margin-top:20px}
/* clients */
.clients{position:absolute;top:1160px;left:0;width:1200px;height:240px;background:var(--white);padding-top:40px}
.client-row{display:flex;align-items:center;justify-content:center;gap:34px;margin-top:48px}
.client{display:flex;align-items:center;gap:6px;font-size:14px;font-weight:600;color:#444}
.client i{width:12px;height:12px;background:#bbb;display:block}
/* products */
.products{position:absolute;top:1400px;left:0;width:1200px;height:820px;background:linear-gradient(180deg,#1b1b1b,#101010)}
.products .section-title{margin-top:60px}
.product-grid{position:absolute;top:150px;left:150px;width:900px;display:grid;grid-template-columns:repeat(3,280px);column-gap:30px;row-gap:50px}
.product h4{font-size:14px;font-weight:600;color:var(--green);margin-bottom:10px}
.product p{font-size:11px;line-height:1.65;color:#bbb}
.dots{position:absolute;bottom:30px;width:100%;display:flex;justify-content:center;gap:8px}
.dots span{width:8px;height:8px;border-radius:50%;background:#555}
.dots span.on{background:var(--white)}
/* footer */
.site-footer{position:absolute;top:2220px;left:0;width:1200px;height:156px;background:var(--green);color:var(--white)}
.footer-col{position:absolute;top:18px}
.footer-col h5{font-size:13px;font-weight:700;margin-bottom:5px}
.footer-col li{list-style:none;font-size:11px;line-height:1.5}
.footer-phone{font-size:22px;font-weight:600}
.footer-brand{position:absolute;right:110px;top:22px;text-align:right}
.footer-brand .brand-name{font-size:32px;color:#1d1d1d}
.social{display:flex;gap:10px;justify-content:flex-end;margin-top:10px;font-size:10px}
.social span{display:flex;align-items:center;gap:4px}
.social i{width:14px;height:14px;border-radius:50%;background:#2a2a2a;display:block}
.copyright{position:absolute;right:110px;bottom:14px;font-size:10px;color:#1d1d1d}
</style>
</head>
<body>

<header class="site-header">
  <div class="logo"><span class="logo-mark"></span><span class="brand-name">Korvadel</span></div>
  <div class="logo-tag">INNOVATIVE SOLUTIONS</div>
  <div class="header-call">
    <span class="phone-icon"><svg width="18" height="18" viewBox="0 0 24 24"><path d="M6.6 10.8a15 15 0 0 0 6.6 6.6l2.2-2.2c.3-.3.7-.4 1-.2 1.1.4 2.3.6 3.6.6.6 0 1 .4 1 1V20c0 .6-.4 1-1 1A17 17 0 0 1 3 4c0-.6.4-1 1-1h3.5c.6 0 1 .4 1 1 0 1.3.2 2.5.6 3.6.1.3 0 .7-.2 1z" fill="#8cc63e"/></svg></span>
    <div><small>Call us at</small><strong>555-014-2290</strong></div>
  </div>
  <nav class="main-nav">
    <a class="active">Home</a><a>About Us</a><a>Products</a><a>Services</a><a>Compliance</a><a>Blog</a><a>Contact</a>
  </nav>
</header>

<section class="hero" role="img" aria-label="Green bokeh light background">
  <svg class="hero-arrow" style="left:50px" width="30" height="60" viewBox="0 0 30 60"><path d="M26 4 4 30l22 26" stroke="#fff" stroke-width="3" fill="none"/></svg>
  <svg class="hero-arrow" style="right:50px" width="30" height="60" viewBox="0 0 30 60"><path d="M4 4l22 26L4 56" stroke="#fff" stroke-width="3" fill="none"/></svg>
  <div class="hero-content">
    <div class="hero-brand"><span class="logo-mark"></span><span class="brand-name">Korvadel</span></div>
    <h1>Korvadel Innovative Solutions</h1>
    <p>The Only Hassle Free Automated Crushing System</p>
  </div>
</section>

<section class="features">
  <div class="feature">
    <svg width="48" height="48" viewBox="0 0 48 48"><rect x="6" y="8" width="36" height="10" fill="#8cc63e"/><rect x="6" y="20" width="36" height="10" fill="#8cc63e"/><rect x="6" y="32" width="36" height="10" fill="#8cc63e"/></svg>
    <h3>Computer Storage Media</h3>
    <p>Safe removal and full destruction of drives, tapes and storage media for secure data disposal.</p>
    <span class="btn">READ MORE</span>
  </div>
  <div class="feature">
    <svg width="48" height="48" viewBox="0 0 48 48"><rect x="8" y="6" width="32" height="36" fill="#8cc63e"/><rect x="14" y="12" width="20" height="4" fill="#fff"/><rect x="14" y="20" width="20" height="4" fill="#fff"/><rect x="14" y="28" width="20" height="4" fill="#fff"/></svg>
    <h3>DriveCrux Degausser</h3>
    <p>Erase magnetic media in seconds with a compact unit built for fast and proven data removal.</p>
    <span class="btn">READ MORE</span>
  </div>
  <div class="feature">
    <svg width="48" height="48" viewBox="0 0 48 48"><rect x="6" y="10" width="36" height="28" fill="#8cc63e"/><path d="M20 17v14l12-7z" fill="#fff"/></svg>
    <h3>Crusher, Shredder and Residual Verification Videos</h3>
    <p>Watch each unit at work and see the verified remains left after every crushing cycle.</p>
    <span class="btn">READ MORE</span>
  </div>
</section>

<section class="about" role="img" aria-label="Dark photo of a person standing in a field at dusk">
  <div class="about-content">
    <h2 class="section-title">ABOUT KORVADEL TECHNOLOGIES</h2>
    <p>Korvadel Technologies, Inc. is a privately held company that designs and builds patented machines for secure data destruction, serving government, business and IT teams who need proof that every drive is gone for good.</p>
    <span class="btn">READ MORE</span>
  </div>
</section>

<section class="clients">
  <h2 class="section-title">OUR CLIENTS INCLUDE</h2>
  <div class="client-row">
    <svg width="14" height="24" viewBox="0 0 14 24"><path d="M12 2 2 12l10 10" stroke="#999" stroke-width="2" fill="none"/></svg>
    <span class="client"><i></i>Vendrix</span>
    <span class="client"><i></i>Sentavio</span>
    <span class="client"><i></i>Lumigrove</span>
    <span class="client"><i></i>Chirpaloo</span>
    <span class="client"><i></i>Halvern Group</span>
    <span class="client"><i></i>Quarnis</span>
    <span class="client"><i></i>Ostrava Labs</span>
    <svg width="14" height="24" viewBox="0 0 14 24"><path d="M2 2l10 10L2 22" stroke="#999" stroke-width="2" fill="none"/></svg>
  </div>
</section>

<section class="products">
  <h2 class="section-title">KORVADEL PRODUCTS</h2>
  <div class="product-grid">
    <div class="product"><h4>DriveCrux</h4><p>The DriveCrux is a desktop data destruction unit that crushes hard drives in seconds. When a computer hard drive is fed into the machine, its patented crushing plates deliver force that leaves the platters and read heads of the drive beyond any recovery.</p><span class="btn-outline">PLAY THE VIDEO</span></div>
    <div class="product"><h4>DriveCrux Compact</h4><p>The DriveCrux Compact is a desktop data destruction unit built for small offices. When a computer hard drive is fed into the machine, its patented crushing plates deliver force that leaves the platters and read heads of the drive beyond any recovery.</p><span class="btn-outline">PLAY THE VIDEO</span></div>
    <div class="product"><h4>DriveCrux</h4><p>The DriveCrux is a desktop data destruction unit that crushes hard drives in seconds. When a computer hard drive is fed into the machine, its patented crushing plates deliver force that leaves the platters and read heads of the drive beyond any recovery.</p><span class="btn-outline">PLAY THE VIDEO</span></div>
    <div class="product"><h4>DriveCrux SSD</h4><p>The DriveCrux SSD is a desktop data destruction unit for solid state media. When a drive is fed into the machine, its patented crushing plates deliver force that breaks every memory chip and board of the drive beyond any recovery.</p><span class="btn-outline">PLAY THE VIDEO</span></div>
    <div class="product"><h4>DriveCrux Compact SSD</h4><p>The DriveCrux Compact SSD is a desktop data destruction unit for small offices. When a drive is fed into the machine, its patented crushing plates deliver force that breaks every memory chip and board of the drive beyond any recovery.</p><span class="btn-outline">PLAY THE VIDEO</span></div>
    <div class="product"><h4>DriveCrux Max SSD</h4><p>The DriveCrux Max SSD is a desktop data destruction unit for high volume sites. When a drive is fed into the machine, its patented crushing plates deliver force that breaks every memory chip and board of the drive beyond any recovery.</p><span class="btn-outline">PLAY THE VIDEO</span></div>
  </div>
  <div class="dots"><span class="on"></span><span></span></div>
</section>

<footer class="site-footer">
  <div class="footer-col" style="left:130px"><h5>QUICK LINKS</h5><ul><li>Home</li><li>About Us</li><li>Our Clients</li><li>Services</li><li>Compliance</li><li>Contact Us</li></ul></div>
  <div class="footer-col" style="left:330px"><h5>PRODUCTS</h5><ul><li>DriveCrux</li><li>DriveCrux Compact</li><li>DriveCrux SSD</li><li>DriveCrux Max SSD</li><li>DriveCrux Degausser</li></ul></div>
  <div class="footer-col" style="left:560px"><h5>CALL US</h5><div class="footer-phone">555-014-2290</div><ul><li>info@korvadel.com</li><li>www.korvadel.com</li></ul></div>
  <div class="footer-brand">
    <div class="brand-name">Korvadel</div>
    <div class="social"><span><i></i>Lumigrove</span><span><i></i>Chirpaloo</span><span><i></i>Streamvault</span></div>
  </div>
  <div class="copyright">© Korvadel.com All Rights Reserved</div>
</footer>

</body>
</html>
```